Maple Hollow Summer Swim Bag Tag Design

Hello!

We are looking to design a 2-sided bag tag for a children's summer swim team. Colors should be blue, white, pink. May also use a lighter blue or navy as an accent if needed. Attached are 2 files showing the look/feel of some of our other items. The bag tag would need to be in line with this same look.

Copy: Maple Hollow Otters Swim 2026
#paddlesout

The copy can be both on one side, or split between the 2 sides, either works. We are flexible! Needs to incorporate the 2026 logo into the design.

```html
<!DOCTYPE html>
<html lang="en">
<head>
<meta charset="utf-8">
<title>Maple Hollow Summer Swim Bag Tag</title>
<link rel="stylesheet" href="https://fonts.googleapis.com/css2?family=Montserrat:wght@400;500;600;700&display=swap">
<style>
  :root {
    --backdrop: #f07fb1;
    --team-blue: #2952a3;
    --team-pink: #ef5a9e;
    --pink-soft: #e266a8;
    --blue-soft: #6a5bb0;
    --white: #ffffff;
  }
  * { margin: 0; padding: 0; box-sizing: border-box; }
  html, body {
    width: 1200px;
    height: 1100px;
    overflow: hidden;
    background: var(--backdrop);
    font-family: "Montserrat", sans-serif;
  }
  .canvas {
    position: relative;
    width: 1200px;
    height: 1100px;
  }
  .tag {
    position: absolute;
    top: 220px;
    width: 422px;
    height: 614px;
    overflow: hidden;
  }
  .tag--front { left: 141px; background: var(--team-blue); }
  .tag--back { left: 636px; }

  .year-mark {
    position: absolute;
    left: 0;
    top: 0;
    width: 422px;
    height: 614px;
  }
  .year-mark text {
    font-family: "Montserrat", sans-serif;
    font-weight: 600;
  }

  .team-name {
    position: absolute;
    left: 0;
    right: 0;
    top: 480px;
    text-align: center;
    color: var(--white);
    font-weight: 500;
    font-size: 30px;
    line-height: 37px;
    letter-spacing: 0.5px;
    text-transform: uppercase;
  }

  .back-art {
    position: absolute;
    inset: 0;
    background: radial-gradient(ellipse at 50% 40%, var(--blue-soft) 0%, var(--pink-soft) 75%);
  }
  .hashtag {
    position: absolute;
    left: 0;
    right: 0;
    top: 430px;
    text-align: center;
    font-weight: 700;
    font-size: 46px;
    line-height: 56px;
    color: var(--team-pink);
    -webkit-text-stroke: 6px var(--white);
    paint-order: stroke fill;
    letter-spacing: -0.5px;
  }

  .tag-label {
    position: absolute;
    top: 900px;
    width: 422px;
    text-align: center;
    color: var(--white);
    font-weight: 500;
    font-size: 34px;
    letter-spacing: 1px;
  }
  .tag-label--front { left: 141px; }
  .tag-label--back { left: 636px; }
</style>
</head>
<body>
<main class="canvas">
  <section class="tag tag--front" aria-label="Bag tag front">
    <svg class="year-mark" viewBox="0 0 422 614" aria-label="2026 with Maple Hollow">
      <text x="84" y="259" font-size="198" fill="var(--white)">2</text>
      <text x="126" y="381" font-size="198" fill="var(--team-pink)">2</text>
      <text x="209" y="429" font-size="212" fill="var(--team-pink)">6</text>
      <circle cx="263" cy="206" r="60" fill="var(--team-blue)" stroke="var(--white)" stroke-width="25"/>
      <text x="263" y="203" font-size="13" fill="var(--white)" text-anchor="middle" letter-spacing="0.5">MAPLE</text>
      <text x="263" y="220" font-size="13" fill="var(--white)" text-anchor="middle" letter-spacing="0.5">HOLLOW</text>
    </svg>
    <p class="team-name">Maple Hollow<br>Otters Swim</p>
  </section>

  <section class="tag tag--back" aria-label="Bag tag back">
    <div class="back-art" role="img" aria-label="Illustration area: leaping team mascot silhouette over pink and blue ripple lines"></div>
    <p class="hashtag">#paddlesout</p>
  </section>

  <p class="tag-label tag-label--front">TAG FRONT</p>
  <p class="tag-label tag-label--back">TAG BACK</p>
</main>
</body>
</html>
```